Management Company for Associations needs new and improved letterhead

We need a design for letterhead that looks professional. We like designs that can incorporate a lot of space for our letters, a new age professional font, and different styles to choose from. Please use the language in the attached letterhead example. The BRV logo needs to be incorporated in the letterhead; please follow the size requirements for use. We are trying to totally revamp our letterhead.
Industry/Entity Type
Property Management
Font styles to use
Serif
Script
Colors
ec1f27
Requirements
Must have
- BRV Logo in black, Q7 logo, Using both Top & Bottom, Red Color used to match logo color.
Nice to have
- (1 design with a watermark using Q7 logo)

```html
<!DOCTYPE html>
<html lang="en">
<head>
<meta charset="utf-8">
<title>Q7 Management Group Letterhead</title>
<link href="https://fonts.googleapis.com/css2?family=Didact+Gothic&family=Roboto:wght@400;700&display=swap" rel="stylesheet">
<style>
  :root {
    --backdrop: #d2d2d2;
    --paper: #f1f1f1;
    --brand-red: #ec1f27;
    --deep-red: #c8121b;
    --ink: #231f20;
    --text: #2b2b2b;
    --rule-grey: #bdbdbd;
  }
  * { margin: 0; padding: 0; box-sizing: border-box; }
  html, body { width: 1200px; height: 1041px; overflow: hidden; }
  body { background: var(--backdrop); position: relative; font-family: "Didact Gothic", sans-serif; color: var(--text); }

  .letterhead { position: absolute; left: 280px; top: 106px; width: 640px; height: 827px; background: var(--paper); overflow: hidden; }

  .brand { position: absolute; left: 51px; top: 38px; display: flex; align-items: center; gap: 10px; }
  .brand-dot { width: 78px; height: 78px; border-radius: 50%; background: var(--brand-red); flex: none; }
  .brand-text { font-family: "Roboto", sans-serif; }
  .brand-name { font-weight: 700; font-size: 19px; color: var(--brand-red); line-height: 1.1; letter-spacing: -0.2px; }
  .brand-tagline { font-size: 9.4px; color: var(--ink); line-height: 1.12; margin-top: 3px; }

  .contact { position: absolute; right: 51px; top: 68px; text-align: right; font-size: 8.6px; line-height: 11.5px; color: var(--ink); font-style: normal; }
  .contact .label, .contact .accent { color: var(--deep-red); font-family: "Roboto", sans-serif; font-weight: 700; }

  .letter { position: absolute; left: 51px; top: 219px; width: 538px; font-size: 9.3px; line-height: 11.2px; }
  .date { margin-bottom: 12px; }
  .recipient { margin-bottom: 56px; }
  .salutation { font-family: "Roboto", sans-serif; font-weight: 700; font-size: 8.6px; margin-bottom: 11px; }
  .body p { text-align: justify; margin-bottom: 11px; }
  .closing { margin-top: 22px; }
  .closing .signer { font-family: "Roboto", sans-serif; font-weight: 700; font-size: 8.6px; }

  .signature { position: absolute; left: 124px; top: 582px; width: 136px; height: 70px; background: linear-gradient(90deg, rgba(125,147,207,0.12), rgba(125,147,207,0.22), rgba(125,147,207,0.1)); border-radius: 6px; }

  .member-badge { position: absolute; left: 51px; top: 740px; width: 106px; height: 44px; background: #dcdcdc; border-radius: 4px; }

  .footer-band { position: absolute; left: 0; bottom: 0; width: 640px; height: 26px; }
  .footer-band .red-rule { height: 4px; background: var(--brand-red); }
  .footer-band .grey-rule { height: 2px; background: var(--rule-grey); margin-top: 2px; }
  .footer-band .dark-bar { height: 18px; background: var(--ink); }
</style>
</head>
<body>
  <main class="letterhead">
    <header>
      <div class="brand">
        <div class="brand-dot"></div>
        <div class="brand-text">
          <div class="brand-name">Q7 Management Group</div>
          <div class="brand-tagline">Dedicated Neighborhood Association<br>Care for Homeowner Boards</div>
        </div>
      </div>
      <address class="contact">
        218 Alder Lane Fairview, OH 44390<br>
        <span class="label">Toll Free:</span> 1.800.555.0142 · <span class="label">Tel:</span> 330.555.0178<br>
        <span class="label">Fax:</span> 330.555.0179 · <span class="label">Email:</span> info@q7mgmt.com<br>
        www.<span class="accent">q7managementgroup</span>.com
      </address>
    </header>

    <section class="letter">
      <p class="date">30.09.2016</p>
      <p class="recipient">Recipient’s name<br>Lindenweg 14<br>10115 Berlin<br>Germany</p>
      <p class="salutation">Dear sir,</p>
      <div class="body">
        <p>Communication is a very integral part of living creatures, animals and humans. Communication may be verbal or written. Written communication however is only applicable to human beings. Can you even imagine a world without communication? Verbal communication can be through telephones, webcams or in person. Written communication is through letters, emails and mobile phone messages.</p>
        <p>In today’s world of great inventions and technology, letters have somehow become redundant. It is the time for text messages or chats. But they still can communicate a lot more than all other modes of communication. Organizations and various government departments still bank on letters as a strong medium of communication. There is no comparison in costs of sending letters as compared to costs of mobile phone messages though – letters are far cheaper. Letters now commonly known as “hard copy documents” are considered more relevant and important than email copies of text messages as proof or evidence of some sort.</p>
        <p>Letters speak volumes about a person or an organization that writes it. So one must take utmost care ensuring that the language used in any letter is appropriate for the occasion for which it is being written. Since a letter is also a written proof or document, if there are certain things that should not form a part of it, then that too should be carefully handled.</p>
        <p>Writing a good letter is an art. But if for some reason someone is unable to write that perfect letter, these different types of letters provide a base for you to build on. Sample letters have been given for everyone to understand what all information needs to form a part of the letter type and then it can be customized.</p>
      </div>
      <p class="closing">Yours Sincerely,<br><span class="signer">Lena Korvath</span></p>
    </section>

    <div class="signature" role="img" aria-label="Handwritten signature in blue ink"></div>

    <div class="member-badge" role="img" aria-label="Association membership badge"></div>

    <footer class="footer-band" aria-hidden="true">
      <div class="red-rule"></div>
      <div class="grey-rule"></div>
      <div class="dark-bar"></div>
    </footer>
  </main>
</body>
</html>
```